Kelvane Plumbing Business cards

Company is Kelvane Plumbing.
name Dashel Morrowby, I am a plumber, drainer, gasfitter and roofer
Mobile: 0431 906 154
Email address: info@kelvaneplumbing.example (check out my website for some ideas)
Website: www.kelvaneplumbing.example
ABN: 82 916 203 471
LIC: 604517K

I am reliable all round plumber. I am a 24 hour emergency service. Kelvane Plumbing is a professional plumbing service in the Illawarra, South Coast, Southern Sydney and Southern Highland regions of NSW. We offer a 24 hour emergency service for piece of mind to our customers. Call us now to see how we can help you. Kelvane Plumbing approaches every job with attention to detail and excellent customer service. With our superior workmanship you can be confident that the job will be done right the first time around. You can rest assured with results that are guaranteed to last.

Target Market(s)

the general public

Contact Information for Business Card

look up website for some ideas something with similar colours to logo and new modern and to catch the eye.

Colors
fdfdfd
ffffff
000000
7f7f7f
aaaaaa
33a6d7
0492cd

Requirements
Must have
• all contact details
• company- Kelvane Plumbing
• name- Dashel Morrowby
• number mobile- 0431 906 154
• Email address- info@kelvaneplumbing.example
• Website- www.kelvaneplumbing.example
• ABN- 82 916 203 471
• LIC- 604517K

```html
<!DOCTYPE html>
<html lang="en">
<head>
<meta charset="utf-8">
<title>Kelvane Plumbing Business Cards</title>
<link rel="stylesheet" href="https://fonts.googleapis.com/css2?family=Open+Sans:wght@400;600;700&display=swap">
<style>
  :root {
    --stage: #1f1f1f;
    --card: #0b0b0b;
    --card-edge: #161616;
    --blue: #0492cd;
    --blue-light: #33a6d7;
    --grey: #7f7f7f;
    --grey-light: #aaaaaa;
    --white: #fdfdfd;
  }
  * { margin: 0; padding: 0; box-sizing: border-box; }
  html, body {
    width: 1200px; height: 1200px; overflow: hidden;
    background: var(--stage);
    font-family: "Open Sans", Arial, sans-serif;
  }
  .stage {
    width: 1200px; height: 1200px;
    display: flex; flex-direction: column; align-items: center; justify-content: center;
    gap: 60px;
  }
  .card {
    width: 820px; height: 500px;
    background: linear-gradient(160deg, var(--card-edge), var(--card) 55%);
    border-radius: 22px;
    position: relative;
    box-shadow: 0 18px 40px rgba(0,0,0,.55);
    overflow: hidden;
  }
  .card-front { display: flex; align-items: center; justify-content: center; }
  .brand-name {
    color: var(--blue);
    font-weight: 700;
    letter-spacing: 0.04em;
    text-transform: uppercase;
    white-space: nowrap;
  }
  .card-front .brand-name { font-size: 54px; }

  .card-back .brand-block {
    position: absolute; left: 50px; top: 110px;
    width: 260px; height: 220px;
    display: flex; align-items: center; gap: 12px;
  }
  .brand-dot {
    width: 22px; height: 22px; border-radius: 50%;
    background: var(--blue); flex: none;
  }
  .card-back .brand-block .brand-name { font-size: 24px; line-height: 1.2; white-space: normal; }
  .divider {
    position: absolute; left: 340px; top: 110px;
    width: 2px; height: 220px; background: var(--grey);
  }
  .contact {
    position: absolute; left: 380px; top: 120px;
    color: var(--white);
  }
  .person-name { color: var(--blue); font-size: 30px; font-weight: 700; line-height: 1.1; }
  .person-role { color: var(--grey); font-size: 19px; margin-bottom: 18px; }
  .contact-list { list-style: none; }
  .contact-list li {
    display: flex; align-items: center; gap: 14px;
    font-size: 20px; line-height: 1.6; letter-spacing: 0.02em;
  }
  .contact-list svg { width: 22px; height: 22px; flex: none; }
  .registration {
    position: absolute; left: 0; right: 0; bottom: 60px;
    text-align: center; color: var(--white);
    font-size: 22px; letter-spacing: 0.04em;
  }
</style>
</head>
<body>
<main class="stage">
  <section class="card card-front">
    <span class="brand-name">Kelvane Plumbing</span>
  </section>

  <section class="card card-back">
    <div class="brand-block">
      <span class="brand-dot"></span>
      <span class="brand-name">Kelvane Plumbing</span>
    </div>
    <div class="divider"></div>
    <div class="contact">
      <p class="person-name">Dashel Morrowby</p>
      <p class="person-role">Plumber, drainer, gasfitter and roofer</p>
      <ul class="contact-list">
        <li>
          <svg viewBox="0 0 24 24" aria-hidden="true"><rect x="6" y="2" width="12" height="20" rx="2" fill="none" stroke="#0492cd" stroke-width="2"/><circle cx="12" cy="18" r="1.2" fill="#0492cd"/></svg>
          0431 906 154
        </li>
        <li>
          <svg viewBox="0 0 24 24" aria-hidden="true"><rect x="2" y="5" width="20" height="14" rx="1" fill="#0492cd"/><path d="M2 5l10 8 10-8" fill="none" stroke="#0b0b0b" stroke-width="1.6"/></svg>
          info@kelvaneplumbing.example
        </li>
        <li>
          <svg viewBox="0 0 24 24" aria-hidden="true"><g fill="none" stroke="#0492cd" stroke-width="1.8"><circle cx="12" cy="12" r="10"/><ellipse cx="12" cy="12" rx="4.5" ry="10"/><path d="M2 12h20M4 7h16M4 17h16"/></g></svg>
          www.kelvaneplumbing.example
        </li>
      </ul>
    </div>
    <p class="registration">ABN - 82 916 203 471 &nbsp;|&nbsp; LIC- 604517K</p>
  </section>
</main>
</body>
</html>
```